Facebook Fan Page for Rantu Vesk, EDM DJ!

I just got a new logo because I plan a reboot in my DJ Career. This also includes a new visual identity in all categories. So in social media. I need a title picture and a profile pic which represent my alias as EDM-DJ. Both should be usable in facebook and twitter as well. It can not be necessary. The graphics should represent my favorite music styles in EDM for example: House, Electro, Electro House, Melbourne Bounce and Big Room. The design should match the new logo which I attached to the project description.

Target Market(s)

Young people who love electronic music and DJ mixes.

Industry/Entity Type

Media

Colors

Designer to choose colors to be used in the design.

Requirements
Must have
• I definitely need graphics to represent my logo and what I'm doing. It should be fit together.
Nice to have
• Complete background design for the facebook and twitter page. Nice to have but not necessary. Maybe implied dj gear in an abstract way.
Should not have
• Funny pictures and a playful or childish appearance. No golden elements.

```html
<!DOCTYPE html>
<html lang="en">
<head>
<meta charset="utf-8">
<title>Rantu Vesk – Social Profile and Cover Options</title>
<link rel="stylesheet" href="https://fonts.googleapis.com/css2?family=Roboto:ital,wght@0,400;0,900;1,300;1,400;1,500;1,700;1,900&display=swap">
<style>
  :root {
    --bg: #000000;
    --frame: #ffffff;
    --brand-blue: #1a72c4;
    --ink: #ffffff;
    --caption: #a6a6a6;
    --teal-soft: #3f8a9c;
    --photo-deep: #040b0d;
    --photo-mid: #1d3d45;
    --photo-light: #5d96a2;
    --photo-glow: #8fc3cc;
  }
  * { box-sizing: border-box; margin: 0; padding: 0; }
  html, body {
    width: 1200px; height: 800px; overflow: hidden;
    background: var(--bg);
    font-family: "Roboto", Arial, sans-serif;
  }
  .board { position: relative; width: 1200px; height: 800px; }

  .option-number {
    position: absolute; top: 90px;
    color: var(--ink);
    font-style: italic; font-weight: 500; font-size: 34px;
    transform: translateX(-50%);
  }

  .profile-tile {
    position: absolute; top: 169px;
    width: 146px; height: 146px;
    border: 1px solid var(--frame);
    background: var(--bg);
    display: flex; flex-direction: column;
    align-items: center; justify-content: center; gap: 8px;
  }
  .mark-dot {
    width: 86px; height: 86px; border-radius: 50%;
    background: var(--brand-blue);
    flex: none;
  }
  .mark-dot.small { width: 62px; height: 62px; }
  .brand-name {
    color: var(--brand-blue);
    font-weight: 900; font-size: 22px; line-height: 1;
    white-space: nowrap; text-align: center;
  }
  .brand-name.stacked { font-size: 36px; line-height: 0.95; }
  .brand-name.stacked-small { font-size: 28px; line-height: 0.95; }

  .cover {
    position: absolute; left: 245px; top: 386px;
    width: 654px; height: 254px;
    border: 1px solid var(--frame);
    overflow: hidden;
    background: var(--photo-deep);
  }
  .cover-photo {
    position: absolute; inset: 0;
    background:
      radial-gradient(ellipse 90px 40px at 28% 42%, var(--photo-glow) 0%, transparent 100%),
      radial-gradient(ellipse 120px 50px at 74% 62%, rgba(143,195,204,0.55) 0%, transparent 100%),
      radial-gradient(ellipse 160px 90px at 38% 12%, var(--photo-light) 0%, transparent 100%),
      radial-gradient(ellipse 200px 110px at 78% 20%, rgba(93,150,162,0.7) 0%, transparent 100%),
      radial-gradient(ellipse 260px 90px at 30% 62%, rgba(29,61,69,0.9) 0%, transparent 100%),
      linear-gradient(180deg, var(--photo-mid) 0%, #10252b 45%, var(--photo-deep) 78%, #000 100%);
  }
  .cover-genres {
    position: absolute; left: 40px; top: 177px;
    color: var(--ink);
    font-style: italic; font-weight: 700; font-size: 11.5px; line-height: 14.5px;
  }
  .cover-rule {
    position: absolute; left: 405px; width: 230px; height: 4px;
    background: var(--brand-blue);
  }
  .cover-rule.top { top: 173px; }
  .cover-rule.bottom { top: 209px; }
  .cover-brand {
    position: absolute; left: 405px; top: 177px; width: 230px;
    text-align: center;
    color: var(--brand-blue);
    font-weight: 900; font-size: 29px; line-height: 32px;
  }
  .cover-role {
    position: absolute; left: 556px; top: 215px;
    color: var(--teal-soft);
    font-style: italic; font-weight: 300; font-size: 20px;
  }

  .cover-caption {
    position: absolute; left: 578px; top: 662px;
    transform: translateX(-50%);
    color: var(--caption);
    font-style: italic; font-weight: 500; font-size: 28px;
    white-space: nowrap;
  }
</style>
</head>
<body>
  <main class="board">
    <div class="option-number" style="left:312px">1</div>
    <div class="option-number" style="left:567px">2</div>
    <div class="option-number" style="left:828px">3</div>

    <section class="profile-tile" style="left:243px" aria-label="Profile picture option 1">
      <span class="mark-dot"></span>
      <span class="brand-name">Rantu Vesk</span>
    </section>

    <section class="profile-tile" style="left:499px" aria-label="Profile picture option 2">
      <span class="brand-name stacked">Rantu<br>Vesk</span>
    </section>

    <section class="profile-tile" style="left:750px" aria-label="Profile picture option 3">
      <span class="mark-dot small"></span>
      <span class="brand-name stacked-small">Rantu<br>Vesk</span>
    </section>

    <section class="cover" aria-label="Cover option 1">
      <div class="cover-photo" role="img" aria-label="Teal-toned photo of a DJ performing at turntables and a mixer above a crowd, with glowing light trails"></div>
      <p class="cover-genres">ELECTRO HOUSE,<br>MELBOURNE BOUNCE<br>AND BIG ROOM</p>
      <span class="cover-rule top"></span>
      <span class="cover-brand">Rantu Vesk</span>
      <span class="cover-rule bottom"></span>
      <span class="cover-role">EDM-DJ</span>
    </section>

    <p class="cover-caption">COVER OPTION 1</p>
  </main>
</body>
</html>
```